TRVW Organisational Values Poster

This design requires logo development for our company values; and graphic design to create the layout suitable for an office poster 1200mm wide and 750mm high.
We are a mental health service with offices in regional and remote Queensland, Australia. We provide services to children and adults of various cultural backgrounds (including Aboriginal Australian) and of various levels of cognitive ability.
For each of our values, we are seeking a logo or icon that will convey the meaning of that word/value. Can the icons you create be easily interpreted by our diverse client population of children and adults, English and non-English speaking??.
Our values are: Collaboration, Learning, Equity, Accountability & Respect. I've uploaded a mock up with websourced logos/icons. Please ensure your work is original so we do not breach any copyright laws.
The resource should also include - less prominently - our company logo; & flags depicting Australia, the Aboriginal, & Torres Strait Island communities; and LGBTQI+ flag. The company logo and flags could sit top right and left of the values list, for example, but these images should appear smaller than the values which are the key message.
Updates
Hi Designers
I have received advice that the preexisting panel, which will host our values poster, is in fact 1200mm wide and 750mm tall.
I apologize for the inconvenience and understand if you choose to withdraw from this project.
If you have time to adjust your design to the new dimensions, your efforts will be appreciated.
Kindly
Gretchen
Target Market(s)
children and adults accessing private mental health services
Look and feel

```html
<!DOCTYPE html>
<html lang="en">
<head>
<meta charset="utf-8">
<title>TRVW Values Poster</title>
<link rel="stylesheet" href="https://fonts.googleapis.com/css2?family=Montserrat:wght@700;800&family=Questrial&display=swap">
<style>
  :root {
    --backdrop: #ededed;
    --paper: #ffffff;
    --purple: #6b4696;
    --purple-soft: #8e6cb5;
    --row-light: #e9f3f2;
    --row-dark: #cbe5e1;
    --brand-green: #2f6b3a;
    --navy: #24265e;
    --flag-red: #cc1b1b;
    --flag-yellow: #ffe500;
    --ts-green: #1f7a3a;
    --ts-blue: #1c3c8c;
  }
  * { margin: 0; padding: 0; box-sizing: border-box; }
  html, body { width: 1200px; height: 1200px; overflow: hidden; background: var(--backdrop); }
  .poster {
    position: absolute; left: 60px; top: 261px;
    width: 1084px; height: 677px;
    background: var(--paper);
    overflow: hidden;
  }
  .brand {
    position: absolute; left: 30px; top: 40px; width: 140px;
    display: flex; flex-direction: column; align-items: center; gap: 6px;
    font-family: "Questrial", sans-serif; color: var(--brand-green);
    font-size: 13px; line-height: 1.15; text-align: center; letter-spacing: 0.3px;
  }
  .brand-dot { width: 26px; height: 26px; border-radius: 50%; background: var(--brand-green); }
  .flags { position: absolute; top: 30px; left: 814px; display: flex; gap: 11px; }
  .flags svg { display: block; width: 51px; height: 32px; }
  .accent-bar { position: absolute; top: 131px; width: 186px; height: 36px; background: var(--purple); }
  .accent-bar.left { left: 0; }
  .accent-bar.right { right: 0; }
  .title {
    position: absolute; left: 0; right: 0; top: 94px;
    text-align: center;
    font-family: "Montserrat", sans-serif; font-weight: 800;
    font-size: 72px; letter-spacing: 1px; color: var(--purple); line-height: 1;
  }
  .values { position: absolute; top: 167px; left: 0; width: 100%; list-style: none; }
  .value {
    position: relative; height: 102px;
    display: flex; align-items: center;
  }
  .value:nth-child(odd) { background: var(--row-light); }
  .value:nth-child(even) { background: var(--row-dark); }
  .value-name {
    position: absolute; left: 312px;
    font-family: "Questrial", sans-serif; font-size: 46px; color: var(--purple);
  }
  .value-name b { font-family: "Montserrat", sans-serif; font-weight: 700; }
  .value-icon {
    position: absolute; top: 12px; height: 78px;
    border-radius: 8px;
    background: linear-gradient(135deg, var(--purple-soft), var(--purple));
    opacity: 0.85;
  }
</style>
</head>
<body>
  <main class="poster">
    <div class="brand">
      <span class="brand-dot"></span>
      <span class="brand-name">Tall River Valley Wellness</span>
    </div>

    <div class="flags">
      <svg viewBox="0 0 51 32" role="img" aria-label="Australian flag">
        <rect width="51" height="32" fill="var(--navy)"/>
        <rect width="26" height="16" fill="var(--navy)"/>
        <path d="M0 0 L26 16 M26 0 L0 16" stroke="#fff" stroke-width="3"/>
        <path d="M0 0 L26 16 M26 0 L0 16" stroke="var(--flag-red)" stroke-width="1"/>
        <path d="M13 0 V16 M0 8 H26" stroke="#fff" stroke-width="5"/>
        <path d="M13 0 V16 M0 8 H26" stroke="var(--flag-red)" stroke-width="3"/>
        <circle cx="13" cy="24" r="2.4" fill="#fff"/>
        <circle cx="38" cy="7" r="1.2" fill="#fff"/>
        <circle cx="44" cy="13" r="1.2" fill="#fff"/>
        <circle cx="33" cy="15" r="1.2" fill="#fff"/>
        <circle cx="39" cy="26" r="1.3" fill="#fff"/>
        <circle cx="41" cy="17" r="0.8" fill="#fff"/>
      </svg>
      <svg viewBox="0 0 51 32" role="img" aria-label="Progress pride flag">
        <rect y="0" width="51" height="5.4" fill="#e40303"/>
        <rect y="5.3" width="51" height="5.4" fill="#ff8c00"/>
        <rect y="10.6" width="51" height="5.4" fill="#ffed00"/>
        <rect y="16" width="51" height="5.4" fill="#008026"/>
        <rect y="21.3" width="51" height="5.4" fill="#24408e"/>
        <rect y="26.6" width="51" height="5.4" fill="#732982"/>
        <path d="M0 -4 L20 16 L0 36 Z" fill="#000"/>
        <path d="M0 -4 L16 16 L0 36 Z" fill="#613915"/>
        <path d="M0 -4 L12 16 L0 36 Z" fill="#74d7ee"/>
        <path d="M0 -4 L8 16 L0 36 Z" fill="#ffafc8"/>
        <path d="M0 0 L4 16 L0 32 Z" fill="#fff"/>
      </svg>
      <svg viewBox="0 0 51 32" role="img" aria-label="Aboriginal flag">
        <rect width="51" height="16" fill="#000"/>
        <rect y="16" width="51" height="16" fill="var(--flag-red)"/>
        <circle cx="25.5" cy="16" r="8" fill="var(--flag-yellow)"/>
      </svg>
      <svg viewBox="0 0 51 32" role="img" aria-label="Torres Strait Islander flag">
        <rect width="51" height="32" fill="var(--ts-green)"/>
        <rect y="4" width="51" height="24" fill="#000"/>
        <rect y="5.5" width="51" height="21" fill="var(--ts-blue)"/>
        <circle cx="25.5" cy="16" r="5" fill="#fff"/>
      </svg>
    </div>

    <div class="accent-bar left"></div>
    <div class="accent-bar right"></div>
    <h1 class="title">TRVW VALUES</h1>

    <ul class="values">
      <li class="value">
        <span class="value-name"><b>C</b>ollaboration</span>
        <span class="value-icon" style="left:676px;width:72px" role="img" aria-label="Icon of three people lifting each other up together"></span>
      </li>
      <li class="value">
        <span class="value-name"><b>L</b>earning</span>
        <span class="value-icon" style="left:691px;width:42px" role="img" aria-label="Icon of a graduate figure reading an open book"></span>
      </li>
      <li class="value">
        <span class="value-name"><b>E</b>quity</span>
        <span class="value-icon" style="left:658px;width:110px" role="img" aria-label="Icon of two figures standing at equal height, one on a step"></span>
      </li>
      <li class="value">
        <span class="value-name"><b>A</b>ccountability</span>
        <span class="value-icon" style="left:670px;width:88px" role="img" aria-label="Icon of a figure beside a checklist of ticked tasks"></span>
      </li>
      <li class="value">
        <span class="value-name"><b>R</b>espect</span>
        <span class="value-icon" style="left:670px;width:88px" role="img" aria-label="Icon of two figures giving each other a high five"></span>
      </li>
    </ul>
  </main>
</body>
</html>
```